E brochure for company overview

We need a brochure for a company overview that will be sent to potential new clients. We are uploading a file with all the content that needs to be included inside of the brochure. We need this content to be displayed in a professional, neat, and creative way. The file has a Spanish and English version so we need two versions of the brochure in each language. *This brochure will be viewed digitally and it will not be printed, thus it does not need a cover page*. We included our company logo (Calvenor) Please utilize this in your design.

```html
<!DOCTYPE html>
<html lang="en">
<head>
<meta charset="utf-8">
<title>Calvenor – Company Overview</title>
<link rel="stylesheet" href="https://fonts.googleapis.com/css2?family=Montserrat:wght@600;700;800&family=Lato:wght@400;700&display=swap">
<style>
:root{
  --orange:#f37021;
  --charcoal:#3a3a3c;
  --ink:#1f1f1f;
  --backdrop:#8c8e90;
  --paper:#ffffff;
  --photo-light:#e9ecec;
  --photo-mid:#a8b0b2;
  --photo-warm:#f4d6b4;
}
*{margin:0;padding:0;box-sizing:border-box}
html,body{width:1200px;height:773px;overflow:hidden;background:var(--backdrop)}
.stage{position:relative;width:1200px;height:773px}
.sheet{position:absolute;top:76px;width:481px;height:622px;background:var(--paper);overflow:hidden;font-family:"Lato",sans-serif;color:var(--ink)}
.sheet--en{left:98px}
.sheet--es{left:617px}

.header{position:absolute;left:0;top:0;width:100%;height:72px}
.brand{position:absolute;left:26px;top:26px;display:flex;align-items:center;gap:7px}
.brand__dot{width:28px;height:28px;border-radius:50%;background:var(--orange)}
.brand__name{font-family:"Montserrat",sans-serif;font-weight:800;font-size:22px;line-height:1;color:var(--charcoal);letter-spacing:.3px}
.brand__tag{position:absolute;left:61px;top:52px;font-family:"Montserrat",sans-serif;font-weight:600;font-size:7.4px;color:var(--charcoal);letter-spacing:.2px}
.header__title{position:absolute;right:22px;top:37px;font-family:"Montserrat",sans-serif;font-weight:700;font-size:10.5px;color:var(--ink)}

.hero{position:absolute;left:0;top:71px;width:100%;height:252px}
.hero__photo{position:absolute;inset:0;background:
  radial-gradient(ellipse 45% 55% at 78% 38%,var(--photo-warm),transparent 70%),
  linear-gradient(180deg,var(--photo-light) 0%,#cfd5d6 45%,var(--photo-mid) 65%,#c4c9c8 100%)}
.hero__frame{position:absolute;inset:0}

.about__item{position:absolute;left:20px;width:254px;font-size:7.9px;line-height:1.4;text-align:justify}
.about__item--history{top:339px}
.about__item--mission{top:391px}
.about__item--vision{top:445px}
.about__item b{font-family:"Montserrat",sans-serif;font-weight:700;color:var(--orange);font-size:8.2px}

.partners-label{position:absolute;left:16px;top:504px;width:143px;height:19px;border-radius:10px;background:var(--orange);color:#fff;font-family:"Montserrat",sans-serif;font-weight:700;font-size:10px;line-height:19px;padding-left:12px}
.partners{position:absolute;left:20px;top:536px;display:flex;align-items:center;gap:12px;font-family:"Lato",sans-serif;font-weight:700;font-size:12px;color:var(--ink)}
.partner{display:flex;align-items:center;gap:4px}
.partner__mark{width:10px;height:10px;border-radius:50%;background:var(--charcoal)}

.services{position:absolute;z-index:2;left:293px;top:323px;width:179px;height:258px;background:var(--charcoal);border-radius:0 0 10px 10px}
.services__tab{position:absolute;left:16px;top:-6px;width:142px;height:25px;background:var(--orange);border-radius:0 0 12px 12px;color:#fff;font-family:"Montserrat",sans-serif;font-weight:700;font-size:10px;line-height:25px;text-align:center}
.services__list{position:absolute;left:9px;top:30px;list-style:none;font-size:8.6px;line-height:11.4px;color:var(--orange)}
.services__list li::before{content:"• "}
.values{position:absolute;left:13px;top:115px;list-style:none}
.values li{display:flex;align-items:center;height:28.6px;gap:9px;font-family:"Montserrat",sans-serif;font-weight:700;font-size:9.4px;color:var(--orange)}
.values svg{width:24px;height:24px;flex:none}

.footer-dark{position:absolute;left:0;bottom:0;width:100%;height:50px}
.footer__title{position:absolute;left:20px;top:584px;font-family:"Montserrat",sans-serif;font-weight:700;font-size:8.4px;letter-spacing:-.15px;color:#fff;white-space:nowrap}
.footer__contacts{position:absolute;left:20px;top:598px;display:flex;gap:22px;font-size:11px;color:#fff}
.contact{display:flex;align-items:center;gap:6px}
.contact svg{width:9px;height:9px}
.footer__web{position:absolute;left:317px;top:598px;display:flex;align-items:center;gap:8px;font-family:"Montserrat",sans-serif;font-weight:700;font-size:13px;color:#fff}
.footer__web svg{width:11px;height:11px}
</style>
</head>
<body>
<main class="stage">

<article class="sheet sheet--en">
  <header class="header">
    <div class="brand"><span class="brand__dot"></span><span class="brand__name">CALVENOR</span></div>
    <div class="brand__tag">IT CONSULTING AND SERVICES</div>
    <h1 class="header__title">COMPLETE MANAGEMENT SYSTEM</h1>
  </header>

  <div class="hero">
    <div class="hero__photo" role="img" aria-label="Businessman in a suit standing in a bright office, facing a network of connected people icons"></div>
    <svg class="hero__frame" viewBox="0 0 481 252" preserveAspectRatio="none">
      <polygon points="0,0 251,0 235,7 0,7" fill="#fff"/>
      <polygon points="251,0 481,0 481,7 235,7" fill="var(--orange)"/>
    </svg>
  </div>

  <p class="about__item about__item--history"><b>HISTORY:</b> Calvenor initiates on 2006<br>Calvenor has 15 years in the technology industry, specialising in security management, infrastructure and service management.</p>
  <p class="about__item about__item--mission"><b>MISSION:</b> Providing our customers with the best human and technological resources with the clear objective of providing effective solutions using best industry practices.</p>
  <p class="about__item about__item--vision"><b>VISION:</b> To be recognized by our customers as an important company in the Dominican Republic in the area of security and infrastructure and achieve presence throughout the Caribbean and Central America.</p>

  <div class="partners-label">OUR PARTNERS:</div>
  <div class="partners">
    <span class="partner"><span class="partner__mark"></span>NORTHVALE</span>
    <span class="partner">ardento</span>
    <span class="partner">kestrelio</span>
    <span class="partner">quill</span>
  </div>

  <aside class="services">
    <div class="services__tab">OUR SERVICES:</div>
    <ul class="services__list">
      <li>Service Management</li>
      <li>Security of Information</li>
      <li>Custom Development</li>
      <li>Device and Network Monitoring</li>
      <li>Devops</li>
      <li>API Management</li>
      <li>Staffing Values</li>
    </ul>
    <ul class="values">
      <li><svg viewBox="0 0 24 24"><circle cx="12" cy="12" r="11" fill="none" stroke="#8a8a8c" stroke-width="1.4"/><circle cx="12" cy="12" r="7" fill="var(--orange)"/></svg>INTEGRITY</li>
      <li><svg viewBox="0 0 24 24"><circle cx="12" cy="12" r="11" fill="none" stroke="#8a8a8c" stroke-width="1.4"/><circle cx="12" cy="12" r="7" fill="var(--orange)"/></svg>CREATIVITY</li>
      <li><svg viewBox="0 0 24 24"><circle cx="12" cy="12" r="11" fill="none" stroke="#8a8a8c" stroke-width="1.4"/><circle cx="12" cy="12" r="7" fill="var(--orange)"/></svg>TEAM WORK</li>
      <li><svg viewBox="0 0 24 24"><circle cx="12" cy="12" r="11" fill="none" stroke="#8a8a8c" stroke-width="1.4"/><circle cx="12" cy="12" r="7" fill="var(--orange)"/></svg>POSITIVE ATTITUDE</li>
      <li><svg viewBox="0 0 24 24"><circle cx="12" cy="12" r="11" fill="none" stroke="#8a8a8c" stroke-width="1.4"/><circle cx="12" cy="12" r="7" fill="var(--orange)"/></svg>COMMITMENT</li>
    </ul>
  </aside>

  <svg class="footer-dark" viewBox="0 0 481 50" preserveAspectRatio="none">
    <polygon points="0,0 278,0 300,50 0,50" fill="var(--charcoal)"/>
    <polygon points="285,20 481,20 481,50 300,50" fill="var(--orange)"/>
  </svg>
  <div class="footer__title">FOR MORE INFORMATION PLEASE CONTACT US</div>
  <div class="footer__contacts">
    <span class="contact"><svg viewBox="0 0 10 10"><circle cx="5" cy="5" r="5" fill="#fff"/><path d="M3.2 2.8l1 .9-.5.7c.4.8 1 1.4 1.8 1.8l.7-.5.9 1-.7.7C4.8 7.2 2.8 5.2 2.6 3.4z" fill="var(--charcoal)"/></svg>809 555 0142</span>
    <span class="contact"><svg viewBox="0 0 10 10"><circle cx="5" cy="5" r="5" fill="#fff"/><rect x="2.5" y="3.3" width="5" height="3.4" fill="none" stroke="var(--charcoal)" stroke-width=".8"/><path d="M2.5 3.3L5 5.3 7.5 3.3" fill="none" stroke="var(--charcoal)" stroke-width=".8"/></svg>info@calvenor.com</span>
  </div>
  <div class="footer__web"><svg viewBox="0 0 12 12"><circle cx="6" cy="6" r="5.2" fill="none" stroke="#fff" stroke-width="1.2"/><path d="M1 6h10M6 1c2.4 2.8 2.4 7.2 0 10M6 1c-2.4 2.8-2.4 7.2 0 10" fill="none" stroke="#fff"/></svg>calvenor.com.do</div>
</article>

<article class="sheet sheet--es" lang="es">
  <header class="header">
    <div class="brand"><span class="brand__dot"></span><span class="brand__name">CALVENOR</span></div>
    <div class="brand__tag">IT CONSULTING AND SERVICES</div>
    <h1 class="header__title">SISTEMA DE GESTIÓN COMPLETO</h1>
  </header>

  <div class="hero">
    <div class="hero__photo" role="img" aria-label="Hombre de negocios de traje en una oficina luminosa frente a una red de iconos de personas conectadas"></div>
    <svg class="hero__frame" viewBox="0 0 481 252" preserveAspectRatio="none">
      <polygon points="0,0 251,0 235,7 0,7" fill="#fff"/>
      <polygon points="251,0 481,0 481,7 235,7" fill="var(--orange)"/>
    </svg>
  </div>

  <p class="about__item about__item--history"><b>HISTORIA:</b> Calvenor inicia en 2006<br>Calvenor tiene 15 años en la industria de la tecnología, especializándose en administración de seguridad, infraestructura y administración de servicios.</p>
  <p class="about__item about__item--mission"><b>MISIÓN:</b> Brindar a nuestros clientes los mejores recursos humanos y tecnológicos con el claro objetivo de brindar soluciones efectivas utilizando las mejores prácticas de la industria.</p>
  <p class="about__item about__item--vision"><b>VISIÓN:</b> Ser reconocidos por nuestros clientes como una empresa importante en República Dominicana en el área de seguridad e infraestructura y lograr presencia en todo el Caribe y Centroamérica.</p>

  <div class="partners-label">NUESTROS SOCIOS:</div>
  <div class="partners">
    <span class="partner"><span class="partner__mark"></span>NORTHVALE</span>
    <span class="partner">ardento</span>
    <span class="partner">kestrelio</span>
    <span class="partner">quill</span>
  </div>

  <aside class="services">
    <div class="services__tab">NUESTROS SERVICIOS:</div>
    <ul class="services__list">
      <li>Gestión de servicios</li>
      <li>Seguridad de la información</li>
      <li>Desarrollo personalizado</li>
      <li>Monitorización de dispositivos y redes</li>
      <li>Devops</li>
      <li>Gestión de API</li>
      <li>Staffing</li>
    </ul>
    <ul class="values">
      <li><svg viewBox="0 0 24 24"><circle cx="12" cy="12" r="11" fill="none" stroke="#8a8a8c" stroke-width="1.4"/><circle cx="12" cy="12" r="7" fill="var(--orange)"/></svg>INTEGRIDAD</li>
      <li><svg viewBox="0 0 24 24"><circle cx="12" cy="12" r="11" fill="none" stroke="#8a8a8c" stroke-width="1.4"/><circle cx="12" cy="12" r="7" fill="var(--orange)"/></svg>CREATIVIDAD</li>
      <li><svg viewBox="0 0 24 24"><circle cx="12" cy="12" r="11" fill="none" stroke="#8a8a8c" stroke-width="1.4"/><circle cx="12" cy="12" r="7" fill="var(--orange)"/></svg>TRABAJO EN EQUIPO</li>
      <li><svg viewBox="0 0 24 24"><circle cx="12" cy="12" r="11" fill="none" stroke="#8a8a8c" stroke-width="1.4"/><circle cx="12" cy="12" r="7" fill="var(--orange)"/></svg>ACTITUD POSITIVA</li>
      <li><svg viewBox="0 0 24 24"><circle cx="12" cy="12" r="11" fill="none" stroke="#8a8a8c" stroke-width="1.4"/><circle cx="12" cy="12" r="7" fill="var(--orange)"/></svg>COMPROMISO</li>
    </ul>
  </aside>

  <svg class="footer-dark" viewBox="0 0 481 50" preserveAspectRatio="none">
    <polygon points="0,0 278,0 300,50 0,50" fill="var(--charcoal)"/>
    <polygon points="285,20 481,20 481,50 300,50" fill="var(--orange)"/>
  </svg>
  <div class="footer__title">PARA MÁS INFORMACIÓN POR FAVOR CONTÁCTENOS</div>
  <div class="footer__contacts">
    <span class="contact"><svg viewBox="0 0 10 10"><circle cx="5" cy="5" r="5" fill="#fff"/><path d="M3.2 2.8l1 .9-.5.7c.4.8 1 1.4 1.8 1.8l.7-.5.9 1-.7.7C4.8 7.2 2.8 5.2 2.6 3.4z" fill="var(--charcoal)"/></svg>809 555 0142</span>
    <span class="contact"><svg viewBox="0 0 10 10"><circle cx="5" cy="5" r="5" fill="#fff"/><rect x="2.5" y="3.3" width="5" height="3.4" fill="none" stroke="var(--charcoal)" stroke-width=".8"/><path d="M2.5 3.3L5 5.3 7.5 3.3" fill="none" stroke="var(--charcoal)" stroke-width=".8"/></svg>info@calvenor.com</span>
  </div>
  <div class="footer__web"><svg viewBox="0 0 12 12"><circle cx="6" cy="6" r="5.2" fill="none" stroke="#fff" stroke-width="1.2"/><path d="M1 6h10M6 1c2.4 2.8 2.4 7.2 0 10M6 1c-2.4 2.8-2.4 7.2 0 10" fill="none" stroke="#fff"/></svg>calvenor.com.do</div>
</article>

</main>
</body>
</html>
```